Skyscraper Banner 160x600 pixels

Wording -
-----------------------------
Click here for Sydney and NSW events,
places to stay and things to see.

Velmorastaysnet.com.au
-------------------------
Tastefull, in blue and red perhaps , Sydney image/s plenty of white space as that looks good, so not too busy.

The wording is important, the emphasis should be on Accommodation or places to stay while events places to go and things to do come after. This will be placed on www.quorvally.com.au, I like a lot of white space with a clear message.

There's been a lot of designs come in and more to come so please be patient.

```html
<!DOCTYPE html>
<html lang="en">
<head>
<meta charset="utf-8">
<title>Skyscraper Banners 160x600</title>
<link rel="stylesheet" href="https://fonts.googleapis.com/css2?family=Oswald:wght@400;500&family=Alegreya:ital,wght@1,400&family=Roboto:wght@400&display=swap">
<style>
  :root {
    --stage: #2a2a2a;
    --white: #ffffff;
    --brand-red: #d9262c;
    --navy: #1d4a86;
    --blue-deep: #0e2466;
    --blue-mid: #2a4fb0;
    --silver-light: #f6f6f6;
    --silver-mid: #d6d6d6;
    --silver-dark: #b8b8b8;
    --ink: #2b2b2b;
    --ring: #c9c9c9;
    --sky: #7fb4e6;
    --sea: #2f7fb6;
    --city: #8a8f86;
    --green: #4e7a3a;
  }
  * { box-sizing: border-box; margin: 0; padding: 0; }
  html, body { width: 1200px; height: 1116px; overflow: hidden; }
  body { background: var(--stage); position: relative; font-family: "Oswald", sans-serif; }

  .banner {
    position: absolute;
    width: 240px;
    height: 900px;
    background: var(--white);
    overflow: hidden;
    box-shadow: 0 6px 18px rgba(0,0,0,0.55);
  }
  .banner--classic { left: 153px; top: 120px; }
  .banner--royal   { left: 474px; top: 120px; }
  .banner--silver  { left: 797px; top: 116px; }

  .brand {
    position: absolute; left: 0; right: 0;
    display: flex; align-items: center; justify-content: center;
    font-family: "Oswald", sans-serif; font-weight: 400;
    font-size: 19px; color: var(--brand-red);
    letter-spacing: 0.2px;
  }

  /* Classic variant */
  .edge-bar { position: absolute; left: 0; right: 0; height: 9px; background: var(--brand-red); }
  .edge-bar--top { top: 0; }
  .edge-bar--bottom { bottom: 0; }
  .banner--classic .brand { top: 9px; height: 129px; }
  .divider { position: absolute; left: 0; right: 0; top: 138px; height: 6px; background: var(--silver-mid); }
  .harbour-photo {
    position: absolute; left: 0; right: 0; top: 144px; height: 399px;
    background: linear-gradient(180deg, var(--sky) 0%, #a9cdef 45%, var(--city) 62%, var(--sea) 68%, #1f6aa0 100%);
  }
  .silver-panel {
    position: absolute; left: 0; right: 0; top: 543px; bottom: 9px;
    background: linear-gradient(90deg, var(--silver-mid) 0%, var(--silver-light) 50%, var(--silver-mid) 100%);
  }
  .headline-caps {
    position: absolute; left: 0; right: 0; top: 62px;
    text-align: center; text-transform: uppercase;
    font-family: "Oswald", sans-serif; font-weight: 400;
    font-size: 30px; line-height: 39px; color: var(--navy);
  }
  .url-red {
    position: absolute; left: 0; right: 0;
    text-align: center; font-family: "Roboto", sans-serif;
    font-size: 17px; color: var(--brand-red);
  }
  .banner--classic .url-red { top: 300px; }

  /* Royal variant */
  .banner--royal .brand, .banner--silver .brand { top: 0; height: 158px; }
  .royal-panel {
    position: absolute; left: 0; right: 0; top: 158px; bottom: 0;
    background: radial-gradient(ellipse at 50% 30%, var(--blue-mid) 0%, var(--blue-deep) 75%);
  }
  .headline-script {
    position: absolute; left: 0; right: 0; top: 20px;
    text-align: center;
    font-family: "Alegreya", serif; font-style: italic;
    font-size: 29px; line-height: 33px; color: var(--white);
  }
  .url-white {
    position: absolute; left: 0; right: 0; top: 683px;
    text-align: center; font-family: "Roboto", sans-serif;
    font-size: 19px; color: var(--white);
  }

  /* Silver variant */
  .silver-full {
    position: absolute; left: 0; right: 0; top: 158px; bottom: 0;
    background: linear-gradient(90deg, var(--silver-dark) 0%, var(--silver-light) 50%, var(--silver-dark) 100%);
    border-top: 3px solid var(--silver-mid);
  }
  .headline-plain {
    position: absolute; left: 0; right: 0; top: 28px;
    text-align: center;
    font-family: "Oswald", sans-serif; font-weight: 400;
    font-size: 29px; line-height: 35px; color: var(--ink);
  }
  .banner--silver .url-red { top: 680px; font-size: 19px; }

  .city-window { position: absolute; left: 0; top: 218px; width: 240px; height: 440px; }
</style>
</head>
<body>

  <section class="banner banner--classic">
    <div class="edge-bar edge-bar--top"></div>
    <div class="brand">Velmorastaysnet.com.au</div>
    <div class="divider"></div>
    <div class="harbour-photo" role="img" aria-label="Sydney city skyline across blue harbour water under a bright sky"></div>
    <div class="silver-panel">
      <p class="headline-caps">Click here for<br>Sydney and NSW<br>events, places<br>to stay and<br>things to see</p>
      <p class="url-red">www.velmorastaysnet.com.au</p>
    </div>
    <div class="edge-bar edge-bar--bottom"></div>
  </section>

  <section class="banner banner--royal">
    <div class="brand">Velmorastaysnet.com.au</div>
    <div class="royal-panel">
      <p class="headline-script">Click here for<br>Sydney and NSW<br>events, places<br>to stay and<br>things to see</p>
      <svg class="city-window" viewBox="0 0 240 440" role="img" aria-label="Aerial view of Sydney city towers and a bridge highway with traffic">
        <defs>
          <linearGradient id="royalCity" x1="0" y1="0" x2="0" y2="1">
            <stop offset="0" stop-color="#8fbde8"/>
            <stop offset="0.3" stop-color="#9a9f9a"/>
            <stop offset="0.7" stop-color="#6f7a62"/>
            <stop offset="1" stop-color="#3f6a34"/>
          </linearGradient>
        </defs>
        <path d="M0,42 Q120,-22 240,42 V398 Q120,462 0,398 Z" fill="var(--ring)"/>
        <path d="M0,56 Q120,-6 240,56 V386 Q120,448 0,386 Z" fill="url(#royalCity)"/>
      </svg>
      <p class="url-white">Velmorastaysnet.com.au</p>
    </div>
  </section>

  <section class="banner banner--silver">
    <div class="brand">Velmorastaysnet.com.au</div>
    <div class="silver-full">
      <p class="headline-plain">Click here for<br>Sydney and NSW<br>events, places<br>to stay and<br>things to see</p>
      <svg class="city-window" viewBox="0 0 240 440" role="img" aria-label="Aerial view of Sydney city towers and a bridge highway with traffic">
        <defs>
          <linearGradient id="silverCity" x1="0" y1="0" x2="0" y2="1">
            <stop offset="0" stop-color="#8fbde8"/>
            <stop offset="0.3" stop-color="#9a9f9a"/>
            <stop offset="0.7" stop-color="#6f7a62"/>
            <stop offset="1" stop-color="#3f6a34"/>
          </linearGradient>
        </defs>
        <path d="M0,42 Q120,-22 240,42 V398 Q120,462 0,398 Z" fill="#a9a9a9"/>
        <path d="M0,56 Q120,-6 240,56 V386 Q120,448 0,386 Z" fill="url(#silverCity)"/>
      </svg>
      <p class="url-red">Velmorastaysnet.com.au</p>
    </div>
  </section>

</body>
</html>
```